Geothermal company needs a creative "POW" business card

Manufacturers tend to be boring. We are not! We are a Geothermal Heat Pump company that has over 30 yrs of experience and wants a new look and updated feel. Nothing old (yawn) so get your creative hats on and let's rock!

We want to use the great colors of lime green and navy blue. Our new logo is attached and we're ready to roll. Remember, we're a professional leader in the geothermal industry that needs to make an eye catching and memorable first glance.

```html
<!DOCTYPE html>
<html lang="en">
<head>
<meta charset="utf-8">
<title>Boreal Loop Business Card</title>
<link href="https://fonts.googleapis.com/css2?family=Source+Sans+3:wght@400;600;700&display=swap" rel="stylesheet">
<style>
  :root {
    --stage: #141414;
    --sky: #1fa6e2;
    --sky-deep: #0b8fd1;
    --navy: #2e5d8f;
    --ink-navy: #17365c;
    --lime: #8cc63f;
    --leaf: #2f8a3a;
    --paper: #ffffff;
    --paper-shade: #e9edf2;
    --text-dark: #1f3348;
  }
  * { margin: 0; padding: 0; box-sizing: border-box; }
  html, body {
    width: 1200px; height: 900px; overflow: hidden;
    background: var(--stage);
    font-family: "Source Sans 3", "Myriad Pro", sans-serif;
  }
  .stage {
    position: relative; width: 1200px; height: 900px;
    display: flex; flex-direction: column; align-items: center; justify-content: center; gap: 56px;
  }
  .card {
    position: relative; width: 525px; height: 300px;
    border-radius: 18px; overflow: hidden;
  }
  /* Back side */
  .card-back { background: var(--sky); }
  .card-back .brand {
    position: absolute; right: 34px; top: 118px; text-align: right;
  }
  .brand-name {
    font-weight: 700; font-size: 40px; color: var(--lime); line-height: 1;
    display: flex; align-items: center; gap: 12px; justify-content: flex-end;
  }
  .brand-dot {
    width: 30px; height: 30px; border-radius: 50%; background: var(--paper);
  }
  .brand-tagline {
    margin-top: 6px; font-size: 13px; color: var(--ink-navy); font-weight: 600;
  }
  /* Front side */
  .card-front { background: var(--paper); }
  .card-front .swoosh { position: absolute; inset: 0; }
  .map-area {
    position: absolute; left: 60px; top: 70px; width: 420px; height: 110px;
    background: radial-gradient(ellipse at center, var(--paper-shade) 0%, rgba(233,237,242,0) 70%);
  }
  .card-front .brand { position: absolute; left: 28px; top: 24px; }
  .card-front .brand-name { justify-content: flex-start; font-size: 38px; }
  .card-front .brand-dot { background: var(--navy); width: 28px; height: 28px; }
  .card-front .brand-tagline { font-size: 12.5px; margin-left: 40px; margin-top: 4px; }
  .person { position: absolute; left: 44px; top: 104px; color: var(--leaf); }
  .person-name { font-size: 17px; font-weight: 400; }
  .person-role { font-size: 11px; }
  .contact {
    position: absolute; right: 26px; bottom: 22px; list-style: none;
    color: var(--ink-navy); font-size: 14px; line-height: 1.22; text-align: right;
  }
  .contact li { display: flex; align-items: center; justify-content: flex-end; gap: 8px; }
  .contact svg { width: 11px; height: 11px; flex: none; }
  .contact .tag { color: var(--lime); font-size: 10px; font-weight: 700; width: 11px; text-align: center; }
</style>
</head>
<body>
<main class="stage">

  <section class="card card-back" aria-label="Card back">
    <div class="brand">
      <div class="brand-name"><span class="brand-dot"></span>Boreal Loop</div>
      <p class="brand-tagline">Manufacturer of Geothermal Heat Pumps for the North</p>
    </div>
  </section>

  <section class="card card-front" aria-label="Card front">
    <div class="map-area" role="img" aria-label="Faint world map backdrop"></div>
    <svg class="swoosh" viewBox="0 0 525 300" aria-hidden="true">
      <path d="M0,140 C150,215 360,220 525,120 L525,300 L0,300 Z" fill="var(--sky-deep)"/>
      <path d="M150,192 C320,215 440,175 525,118 L525,150 C430,200 300,215 150,192 Z" fill="var(--navy)"/>
      <path d="M0,140 C150,215 360,220 525,120" fill="none" stroke="#0d1f33" stroke-width="1.5"/>
    </svg>
    <div class="brand">
      <div class="brand-name"><span class="brand-dot"></span>Boreal Loop</div>
      <p class="brand-tagline">Manufacturer of Geothermal Heat Pumps for the North</p>
    </div>
    <div class="person">
      <p class="person-name">Sam Ridley</p>
      <p class="person-role">CEO</p>
    </div>
    <ul class="contact">
      <li>42 N Birch Ave<svg viewBox="0 0 10 10" style="visibility:hidden"></svg></li>
      <li>Milton, MN 56000
        <svg viewBox="0 0 10 10"><path d="M5,0.5 C2.6,0.5 1.2,2.2 1.2,4 C1.2,6.5 5,9.5 5,9.5 C5,9.5 8.8,6.5 8.8,4 C8.8,2.2 7.4,0.5 5,0.5 Z" fill="var(--lime)"/><circle cx="5" cy="4" r="1.4" fill="var(--sky-deep)"/></svg></li>
      <li>Phone: (555) 014-2200
        <svg viewBox="0 0 10 10"><rect x="1" y="1.5" width="8" height="7" rx="1.5" fill="var(--lime)"/><rect x="3" y="3" width="4" height="2" fill="var(--sky-deep)"/></svg></li>
      <li>Fax: (555) 014-2201<span class="tag">Fx</span></li>
      <li>samridley@borealloop.com
        <svg viewBox="0 0 10 10"><rect x="0.8" y="2" width="8.4" height="6" rx="1" fill="var(--lime)"/><path d="M1,2.3 L5,5.5 L9,2.3" fill="none" stroke="var(--sky-deep)" stroke-width="0.9"/></svg></li>
      <li>www.borealloop.com
        <svg viewBox="0 0 10 10"><circle cx="5" cy="5" r="4.2" fill="var(--lime)"/><path d="M1,5 H9 M5,1 V9" stroke="var(--sky-deep)" stroke-width="0.8"/></svg></li>
    </ul>
  </section>

</main>
</body>
</html>
```